Preoperative Medical clearance for Patients on blood thinners

Prepare a flow chart which directs medical office staff to properly triage patients preparing for surgery who are on blood thinners. We will provide a rudimentary flow chart with all necessary information. We need a better layout which is more appealing and intuitive.

Target Market(s)

internal office use

Industry/Entity Type

Medical

Font styles to use
Sans Serif

Requirements
Must have
• attractive, intuitive layout
Should not have
• things that promote confusion

```html
<!DOCTYPE html>
<html lang="en">
<head>
<meta charset="utf-8">
<title>Preoperative Medical Clearance for Patients on Blood Thinners</title>
<link rel="stylesheet" href="https://fonts.googleapis.com/css2?family=Lato:wght@400&display=swap">
<style>
  :root {
    --node-fill: #7290d0;
    --node-text: #ffffff;
    --connector: #6f8ecf;
    --label: #7f9bd8;
    --backdrop-light: #f7f7f8;
    --backdrop-mid: #eceef2;
  }
  html, body {
    margin: 0;
    padding: 0;
    overflow: hidden;
    background: var(--backdrop-light);
  }
  .canvas {
    position: relative;
    width: 1200px;
    height: 1000px;
    overflow: hidden;
    font-family: "Lato", sans-serif;
  }
  .backdrop {
    position: absolute;
    inset: 0;
    background: radial-gradient(ellipse at 60% 55%, var(--backdrop-mid) 0%, var(--backdrop-light) 70%);
  }
  .flowchart {
    position: absolute;
    inset: 0;
  }
  .connector {
    stroke: var(--connector);
    stroke-width: 3.5;
    fill: none;
  }
  .node {
    fill: var(--node-fill);
  }
  .node-text {
    fill: var(--node-text);
    font-family: "Lato", sans-serif;
    font-size: 18.5px;
    text-anchor: middle;
  }
  .branch-label {
    fill: var(--label);
    font-family: "Lato", sans-serif;
    font-size: 22px;
    letter-spacing: 0.5px;
  }
</style>
</head>
<body>
<main class="canvas">
  <div class="backdrop" role="img" aria-label="Soft pale photograph of a stethoscope lying on a white surface"></div>

  <svg class="flowchart" width="1200" height="1000" viewBox="0 0 1200 1000" aria-label="Preoperative clearance flow chart for patients on blood thinners">
    <g class="connectors">
      <line class="connector" x1="615" y1="122" x2="395" y2="225"/>
      <line class="connector" x1="615" y1="122" x2="970" y2="225"/>
      <line class="connector" x1="395" y1="225" x2="225" y2="388"/>
      <line class="connector" x1="395" y1="225" x2="657" y2="388"/>
      <line class="connector" x1="395" y1="225" x2="997" y2="388"/>
      <line class="connector" x1="225" y1="388" x2="222" y2="542"/>
      <line class="connector" x1="225" y1="388" x2="492" y2="541"/>
      <line class="connector" x1="657" y1="388" x2="492" y2="541"/>
      <line class="connector" x1="997" y1="388" x2="492" y2="541"/>
      <line class="connector" x1="657" y1="388" x2="812" y2="652"/>
      <line class="connector" x1="997" y1="388" x2="1045" y2="712"/>
      <line class="connector" x1="492" y1="541" x2="350" y2="720"/>
      <line class="connector" x1="492" y1="541" x2="638" y2="815"/>
      <line class="connector" x1="346" y1="720" x2="346" y2="890"/>
    </g>

    <g class="branch-labels">
      <text class="branch-label" x="443" y="130">YES</text>
      <text class="branch-label" x="766" y="140">NO</text>
      <text class="branch-label" x="602" y="222">BLEEDING</text>
      <text class="branch-label" x="602" y="252">DISORDER</text>
      <text class="branch-label" x="146" y="297">CARDIAC</text>
      <text class="branch-label" x="426" y="302">STROKE</text>
      <text class="branch-label" x="368" y="437">NO</text>
      <text class="branch-label" x="529" y="437">NO</text>
      <text class="branch-label" x="855" y="396">NO</text>
      <text class="branch-label" x="154" y="469">YES</text>
      <text class="branch-label" x="762" y="548">YES</text>
      <text class="branch-label" x="1038" y="488">YES</text>
      <text class="branch-label" x="334" y="622">YES</text>
      <text class="branch-label" x="556" y="671">NO</text>
    </g>

    <g class="decision">
      <ellipse class="node" cx="615" cy="122" rx="85" ry="60"/>
      <text class="node-text" x="615" y="117">Patient taking</text>
      <text class="node-text" x="615" y="140">a blood thinner?</text>
    </g>
    <g class="terminal">
      <ellipse class="node" cx="970" cy="225" rx="85" ry="60"/>
      <text class="node-text" x="970" y="232">End</text>
    </g>
    <g class="decision">
      <ellipse class="node" cx="395" cy="225" rx="85" ry="60"/>
      <text class="node-text" x="395" y="214">Cardiac problem,</text>
      <text class="node-text" x="395" y="236">bleeding disorder</text>
      <text class="node-text" x="395" y="258">or stroke?</text>
    </g>
    <g class="decision">
      <ellipse class="node" cx="225" cy="388" rx="85" ry="60"/>
      <text class="node-text" x="225" y="373">Have</text>
      <text class="node-text" x="225" y="396">a cardiologist?</text>
    </g>
    <g class="decision">
      <ellipse class="node" cx="657" cy="388" rx="85" ry="60"/>
      <text class="node-text" x="657" y="373">Have</text>
      <text class="node-text" x="657" y="396">neurologist?</text>
    </g>
    <g class="decision">
      <ellipse class="node" cx="997" cy="388" rx="85" ry="60"/>
      <text class="node-text" x="997" y="373">Have</text>
      <text class="node-text" x="997" y="396">a hematologist?</text>
    </g>
    <g class="action">
      <ellipse class="node" cx="222" cy="542" rx="85" ry="60"/>
      <text class="node-text" x="222" y="524">Refer to</text>
      <text class="node-text" x="222" y="546">Patient's current</text>
      <text class="node-text" x="222" y="568">cardiologist</text>
    </g>
    <g class="decision">
      <ellipse class="node" cx="492" cy="541" rx="85" ry="60"/>
      <text class="node-text" x="492" y="522">Have</text>
      <text class="node-text" x="492" y="545">a primary care</text>
      <text class="node-text" x="492" y="568">doctor?</text>
    </g>
    <g class="action">
      <ellipse class="node" cx="812" cy="652" rx="85" ry="60"/>
      <text class="node-text" x="812" y="645">Refer to</text>
      <text class="node-text" x="812" y="668">neurologist</text>
    </g>
    <g class="action">
      <ellipse class="node" cx="1045" cy="712" rx="85" ry="60"/>
      <text class="node-text" x="1045" y="694">Refer to</text>
      <text class="node-text" x="1045" y="717">hematologist</text>
      <text class="node-text" x="1045" y="743">for clearance</text>
    </g>
    <g class="action">
      <ellipse class="node" cx="350" cy="720" rx="85" ry="60"/>
      <text class="node-text" x="350" y="697">Call primary</text>
      <text class="node-text" x="350" y="719">and ask for</text>
      <text class="node-text" x="350" y="741">preferred</text>
      <text class="node-text" x="350" y="763">cardiologist</text>
    </g>
    <g class="action">
      <ellipse class="node" cx="638" cy="815" rx="85" ry="60"/>
      <text class="node-text" x="638" y="801">Select specialist</text>
      <text class="node-text" x="638" y="824">and refer to</text>
      <text class="node-text" x="638" y="847">establish care</text>
    </g>
    <g class="action">
      <ellipse class="node" cx="346" cy="890" rx="85" ry="60"/>
      <text class="node-text" x="346" y="876">Refer to</text>
      <text class="node-text" x="346" y="899">Patient's current</text>
      <text class="node-text" x="346" y="922">cardiologist</text>
    </g>
  </svg>
</main>
</body>
</html>
```